Professional and creatice Life Coach - Business Card design

I just relaunched my website and now i a need a correspoonding business card for my task as life coach. My website is www.tbalrond.com as reference. The compass is kind of a symbol for my work, as I help people navigate through their challenging phases in life. The business card should be colorful, but not too playful as I also adress business people. So it sould be creative, but professional (also to suport my other business as Management Consultant)

Target Market(s)

People who want to get teir problems resolved, in business, partnership and other personal realms

Industry/Entity Type

Life Coaching

Contact Information for Business Card

Front side should include Name, Phone number, Email, Website and address

Font styles to use
Sans Serif

Colors
add136

Requirements
Must have
• "Mag. Leopold Brantner" -> Name
"Energetische Praxis" -> Jobtitle (describing my profession as life coach)
colours and style should match my website www.tbalrond.com
Nice to have
• a compass as a symbol

```html
<!DOCTYPE html>
<html lang="de">
<head>
<meta charset="utf-8">
<title>Leopold Brantner – Visitenkarte</title>
<link href="https://fonts.googleapis.com/css2?family=Roboto:wght@400&family=Saira+Semi+Condensed:wght@600&display=swap" rel="stylesheet">
<style>
  :root {
    --backdrop: #6a6768;
    --card-green: #a4d35c;
    --card-white: #f8f8f7;
    --accent: #8cc63f;
    --ink: #3e4246;
    --ink-soft: #45494d;
  }
  * { margin: 0; padding: 0; box-sizing: border-box; }
  html, body { width: 1200px; height: 1200px; overflow: hidden; }
  body {
    background: var(--backdrop);
    position: relative;
    font-family: "Roboto", sans-serif;
  }
  .card {
    position: absolute;
    border-radius: 22px;
  }
  .card--back {
    left: 238px; top: 118px; width: 712px; height: 419px;
    background: var(--card-green);
    display: flex; align-items: center; justify-content: center;
  }
  .card--front {
    left: 232px; top: 645px; width: 710px; height: 415px;
    background: var(--card-white);
  }
  .brand {
    display: flex; align-items: center; gap: 14px;
    font-family: "Saira Semi Condensed", sans-serif;
    font-weight: 600;
    color: var(--ink);
  }
  .brand__dot {
    border-radius: 50%;
    background: var(--ink);
  }
  .card--back .brand { font-size: 56px; }
  .card--back .brand__dot { width: 34px; height: 34px; }
  .card--front .brand {
    position: absolute; left: 88px; top: 180px;
    font-size: 40px;
  }
  .card--front .brand__dot { width: 26px; height: 26px; background: var(--accent); }
  .contact-block {
    position: absolute; left: 357px; top: 108px;
  }
  .contact-block__name {
    font-family: "Saira Semi Condensed", sans-serif;
    font-weight: 600;
    font-size: 27px;
    line-height: 1;
    color: var(--accent);
  }
  .contact-block__title {
    margin-top: 8px;
    font-size: 18px;
    color: var(--ink-soft);
  }
  .contact-list {
    list-style: none;
    margin-top: 35px;
  }
  .contact-list li {
    display: flex; align-items: center; gap: 14px;
    font-size: 18px; line-height: 26.5px;
    color: var(--ink);
  }
  .contact-list svg { width: 17px; height: 17px; fill: var(--accent); flex: none; margin-left: 2px; }
  .contact-block__address {
    margin-top: 8px;
    font-size: 18px;
    color: var(--ink);
  }
</style>
</head>
<body>
  <section class="card card--back">
    <div class="brand"><span class="brand__dot"></span>Brantner</div>
  </section>

  <section class="card card--front">
    <div class="brand"><span class="brand__dot"></span>Brantner</div>

    <div class="contact-block">
      <h1 class="contact-block__name">Mag. Leopold Brantner</h1>
      <p class="contact-block__title">Energetische Praxis</p>
      <ul class="contact-list">
        <li>
          <svg viewBox="0 0 20 20" aria-hidden="true"><path d="M3 7c0-2 3-4 7-4s7 2 7 4v1h-4V6.5C12 6 11 5.8 10 5.8S8 6 7 6.5V8H3z M6 9h8l3 6v2H3v-2z M10 11a2 2 0 1 0 0 4 2 2 0 0 0 0-4z"/></svg>
          +43 660 3184720
        </li>
        <li>
          <svg viewBox="0 0 20 20" aria-hidden="true"><path d="M2 4h16v1.5l-8 5.5-8-5.5z M2 7.5l8 5.5 8-5.5V16H2z"/></svg>
          leopold@tbalrond.one
        </li>
        <li>
          <svg viewBox="0 0 20 20" aria-hidden="true"><path d="M10 2a8 8 0 1 0 0 16 8 8 0 0 0 0-16zm5.9 7h-3c-.1-2.2-.6-4.1-1.4-5.3A6.5 6.5 0 0 1 15.9 9zM10 3.6c.7.8 1.3 2.8 1.4 5.4H8.6c.1-2.6.7-4.6 1.4-5.4zM8.5 3.7C7.7 4.9 7.2 6.8 7.1 9h-3a6.5 6.5 0 0 1 4.4-5.3zM4.1 11h3c.1 2.2.6 4.1 1.4 5.3A6.5 6.5 0 0 1 4.1 11zm5.9 5.4c-.7-.8-1.3-2.8-1.4-5.4h2.8c-.1 2.6-.7 4.6-1.4 5.4zm1.5-.1c.8-1.2 1.3-3.1 1.4-5.3h3a6.5 6.5 0 0 1-4.4 5.3z"/></svg>
          www.tbalrond.com
        </li>
      </ul>
      <p class="contact-block__address">Lindenweg 12, 5020 Salzburg, Österreich</p>
    </div>
  </section>
</body>
</html>
```